Business Card Design

redesign of card and recreation of logo based on image provided. the business is located in new york so the Brooklyn Bridge figures prominently in the scheme. product should be very clean.

Industry/Entity Type

Real Estate

Contact Information for Business Card

Wendell Ortwick 318 Tamsin Street Brooklyn, New York 11409 wendell@qorvane.com Mobile: 917-555-0143

Colors
cadf82
1b1b1b
ffffff

Requirements
Nice to have
• Brooklyn Bridge

```html
<!DOCTYPE html>
<html lang="en">
<head>
<meta charset="utf-8">
<title>Qorvane &amp; Associates – Business Cards</title>
<link rel="stylesheet" href="https://fonts.googleapis.com/css2?family=Montserrat:wght@300;400&display=swap">
<style>
  :root {
    --backdrop: #333333;
    --paper: #f4f4f2;
    --ink: #1b1b1b;
    --lime: #b5b52a;
    --bridge-light: #c9c9c9;
    --bridge-dark: #8a8a8a;
  }
  * { box-sizing: border-box; margin: 0; padding: 0; }
  html, body {
    width: 1200px; height: 900px; overflow: hidden;
    background: var(--backdrop);
    font-family: "Montserrat", "Helvetica Neue", Arial, sans-serif;
    font-weight: 300;
    color: var(--ink);
  }
  .card {
    position: absolute;
    background: var(--paper);
    box-shadow: 0 6px 18px rgba(0,0,0,.35);
  }
  .bridge-art {
    position: absolute;
    background: linear-gradient(160deg, var(--bridge-light), var(--bridge-dark));
    opacity: .55;
  }

  /* Front */
  .card--front { left: 60px; top: 40px; width: 560px; height: 320px; }
  .card--front .bridge-art { left: 170px; top: 70px; width: 220px; height: 95px; }
  .card--front .wordmark {
    position: absolute; left: 0; right: 0; top: 190px;
    text-align: center; font-size: 26px; letter-spacing: .5px;
  }

  /* Back */
  .card--back { left: 480px; top: 420px; width: 660px; height: 377px; }
  .card--back .bridge-art { left: 300px; top: 28px; width: 320px; height: 135px; }
  .rule { position: absolute; height: 1px; background: var(--ink); }
  .rule--upper { left: 290px; right: 30px; top: 175px; }
  .rule--lower { left: 28px; right: 260px; top: 272px; }
  .contact { position: absolute; left: 40px; top: 110px; font-size: 13px; line-height: 1.45; }
  .contact__name { font-size: 16px; text-transform: uppercase; }
  .contact__role { color: var(--lime); font-size: 11px; text-transform: uppercase; margin-bottom: 14px; }
  .contact__block + .contact__block { margin-top: 10px; }
  .card--back .wordmark {
    position: absolute; left: 36px; top: 292px;
    font-size: 44px; letter-spacing: .5px; white-space: nowrap;
  }
</style>
</head>
<body>
  <section class="card card--front" aria-label="Card front">
    <div class="bridge-art" role="img" aria-label="Grey engraved illustration of a suspension bridge"></div>
    <p class="wordmark">QORVANE &amp; ASSOCIATES</p>
  </section>

  <section class="card card--back" aria-label="Card back">
    <div class="bridge-art" role="img" aria-label="Grey engraved illustration of a suspension bridge"></div>
    <div class="rule rule--upper"></div>
    <div class="contact">
      <p class="contact__name">Wendell Ortwick</p>
      <p class="contact__role">Broker</p>
      <p class="contact__block">318 Tamsin Street<br>Brooklyn, New York 11409</p>
      <p class="contact__block">wendell@qorvane.com<br>Mobile: 917-555-0143</p>
    </div>
    <div class="rule rule--lower"></div>
    <p class="wordmark">QORVANE &amp; ASSOCIATES</p>
  </section>
</body>
</html>
```